Airwave Harbor company needs ad for trade publication

Airwave Harbor provides sales, content, production, technology, and promotion products and services to radio stations to help increase sales and solutions to improve operations and reduce costs. We are looking for a creative ad (sizes 720x250, 300x250, 728x180) with a halloween theme. An angle could be "Nothing Scarier than starting the new year in the RED" which in business terms is a net operating loss. OR "Take a bite out of your 2024 budget". Airwave Harbor CAN HELP!
We want to highlight on the ad 3 key benefits that Airwave Harbor can help (1) "Improve your NTR" (2) "Improve your cash flow" (3) "Improve your technology and operations"
Target Market(s)
Targeting radio stations during their 2024 budgeting process
Look and feel

```html
<!DOCTYPE html>
<html lang="en">
<head>
<meta charset="utf-8">
<title>Airwave Harbor – Nothing Scarier Than Starting the New Year in the Red</title>
<link rel="stylesheet" href="https://fonts.googleapis.com/css2?family=Creepster&family=Jost:wght@400;500;600&display=swap">
<style>
  :root {
    --page: #ffffff;
    --night-top: #1d4450;
    --night-mid: #14262f;
    --night-low: #121218;
    --chart-glow: #3a1216;
    --blood: #e60d0d;
    --arrow-dark: #5a0000;
    --arrow-bright: #e50b0b;
    --copy: #ffffff;
    --copy-soft: #d9dde2;
    --brand: #1f8bef;
  }
  * { margin: 0; padding: 0; box-sizing: border-box; }
  html, body { width: 812px; height: 1200px; overflow: hidden; background: var(--page); }
  .sheet { position: relative; width: 812px; height: 1200px; }

  .ad { position: absolute; left: 41px; width: 730px; overflow: hidden; }
  .ad--large  { top: 42px;  height: 609px; }
  .ad--banner { top: 688px; height: 254px; }
  .ad--leader { top: 979px; height: 180px; }

  .ad__scene {
    position: absolute; inset: 0;
    background:
      radial-gradient(ellipse 60% 45% at 60% 78%, var(--chart-glow) 0%, transparent 70%),
      radial-gradient(circle at 50% 4%, #6f8f8f 0%, transparent 18%),
      linear-gradient(180deg, var(--night-top) 0%, var(--night-mid) 38%, var(--night-low) 62%, var(--night-low) 100%);
  }
  .ad--banner .ad__scene, .ad--leader .ad__scene {
    background:
      radial-gradient(ellipse 60% 55% at 60% 85%, var(--chart-glow) 0%, transparent 70%),
      linear-gradient(180deg, var(--night-top) 0%, var(--night-mid) 35%, var(--night-low) 70%);
  }

  .ad__arrow { position: absolute; inset: 0; width: 100%; height: 100%; }

  .ad__line { position: absolute; white-space: nowrap; line-height: 1; transform: translateX(-50%); }
  .ad__scare, .ad__red {
    font-family: "Creepster", system-ui, cursive; color: var(--blood);
    transform: translateX(-50%) scaleY(1.3); transform-origin: 50% 0;
  }
  .ad__start { font-family: "Jost", Arial, sans-serif; font-weight: 400; color: var(--copy); }

  .brand {
    position: absolute; font-family: "Jost", Arial, sans-serif; font-weight: 600;
    color: var(--brand); text-transform: uppercase; line-height: 0.95; text-align: center;
  }

  .help { position: absolute; font-family: "Jost", Arial, sans-serif; color: var(--copy); }
  .help__title { font-weight: 600; text-transform: uppercase; color: var(--copy); }
  .help__title em { font-style: normal; color: var(--blood); }
  .help__list { list-style: none; }
  .help__item { position: relative; padding-left: 14px; color: var(--copy-soft); font-weight: 500; line-height: 1.2; }
  .help__item::before {
    content: ""; position: absolute; left: 0; top: 0.45em;
    width: 7px; height: 7px; background: var(--blood);
  }

  /* large 730 x 609 */
  .ad--large .ad__scare { left: 360px; top: 222px; font-size: 54px; }
  .ad--large .ad__start { left: 359px; top: 288px; font-size: 46px; }
  .ad--large .ad__red   { left: 359px; top: 352px; font-size: 72px; }
  .ad--large .brand { left: 559px; top: 40px; width: 130px; font-size: 27px; }
  .ad--large .help { left: 30px; right: 30px; top: 500px; text-align: center; }
  .ad--large .help__title { font-size: 22px; margin-bottom: 12px; }
  .ad--large .help__list { display: flex; justify-content: center; gap: 26px; }
  .ad--large .help__item { font-size: 16px; text-align: left; }

  /* banner 730 x 254 */
  .ad--banner .ad__scare { left: 365px; top: 60px;  font-size: 41px; }
  .ad--banner .ad__start { left: 357px; top: 107px; font-size: 33px; }
  .ad--banner .ad__red   { left: 350px; top: 146px; font-size: 46px; }
  .ad--banner .brand { left: 632px; top: 20px; width: 84px; font-size: 15px; }
  .ad--banner .help { left: 16px; top: 70px; width: 166px; }

  /* leaderboard 730 x 180 */
  .ad--leader .ad__scare { left: 365px; top: 28px;  font-size: 41px; }
  .ad--leader .ad__start { left: 357px; top: 70px;  font-size: 33px; }
  .ad--leader .ad__red   { left: 350px; top: 106px; font-size: 46px; }
  .ad--leader .brand { left: 624px; top: 16px; width: 84px; font-size: 15px; }
  .ad--leader .help { left: 16px; top: 36px; width: 166px; }

  .ad--banner .help__title, .ad--leader .help__title { font-size: 14px; margin-bottom: 7px; line-height: 1.15; }
  .ad--banner .help__item, .ad--leader .help__item { font-size: 12px; margin-bottom: 4px; }
</style>
</head>
<body>
<main class="sheet">

  <section class="ad ad--large">
    <div class="ad__scene" role="img" aria-label="Moonlit Halloween night with a haunted house and graveyard above a glowing red falling stock chart"></div>
    <svg class="ad__arrow" viewBox="0 0 730 609" aria-hidden="true">
      <defs>
        <linearGradient id="arrow-large" x1="0" y1="0" x2="1" y2="1">
          <stop offset="0" stop-color="var(--arrow-dark)"/>
          <stop offset="1" stop-color="var(--arrow-bright)"/>
        </linearGradient>
      </defs>
      <polyline points="400,340 560,440 594,406 655,466" fill="none" stroke="url(#arrow-large)" stroke-width="26"/>
      <polygon points="629,500 686,485 676,418" fill="var(--arrow-bright)"/>
    </svg>
    <p class="ad__line ad__scare">NOTHING SCARIER THAN</p>
    <p class="ad__line ad__start">Starting the New Year</p>
    <p class="ad__line ad__red">IN THE RED</p>
    <p class="brand">Airwave<br>Harbor</p>
    <div class="help">
      <p class="help__title">Airwave Harbor <em>can help!</em></p>
      <ul class="help__list">
        <li class="help__item">Improve your NTR</li>
        <li class="help__item">Improve your cash flow</li>
        <li class="help__item">Improve your technology and operations</li>
      </ul>
    </div>
  </section>

  <section class="ad ad--banner">
    <div class="ad__scene" role="img" aria-label="Moonlit Halloween night with a haunted house above a glowing red falling stock chart"></div>
    <svg class="ad__arrow" viewBox="0 0 730 254" aria-hidden="true">
      <defs>
        <linearGradient id="arrow-banner" x1="0" y1="0" x2="1" y2="1">
          <stop offset="0" stop-color="var(--arrow-dark)"/>
          <stop offset="1" stop-color="var(--arrow-bright)"/>
        </linearGradient>
      </defs>
      <polyline points="440,118 514,190 542,163 592,210" fill="none" stroke="url(#arrow-banner)" stroke-width="20"/>
      <polygon points="572,230 614,222 606,170" fill="var(--arrow-bright)"/>
    </svg>
    <p class="ad__line ad__scare">NOTHING SCARIER THAN</p>
    <p class="ad__line ad__start">Starting the New Year</p>
    <p class="ad__line ad__red">IN THE RED</p>
    <p class="brand">Airwave<br>Harbor</p>
    <div class="help">
      <p class="help__title">Airwave Harbor<br><em>can help!</em></p>
      <ul class="help__list">
        <li class="help__item">Improve your NTR</li>
        <li class="help__item">Improve your cash flow</li>
        <li class="help__item">Improve your technology and operations</li>
      </ul>
    </div>
  </section>

  <section class="ad ad--leader">
    <div class="ad__scene" role="img" aria-label="Halloween night sky with a haunted house above a glowing red falling stock chart"></div>
    <svg class="ad__arrow" viewBox="0 0 730 180" aria-hidden="true">
      <defs>
        <linearGradient id="arrow-leader" x1="0" y1="0" x2="1" y2="1">
          <stop offset="0" stop-color="var(--arrow-dark)"/>
          <stop offset="1" stop-color="var(--arrow-bright)"/>
        </linearGradient>
      </defs>
      <polyline points="478,82 568,150 598,122 640,158" fill="none" stroke="url(#arrow-leader)" stroke-width="20"/>
      <polygon points="614,174 660,167 650,120" fill="var(--arrow-bright)"/>
    </svg>
    <p class="ad__line ad__scare">NOTHING SCARIER THAN</p>
    <p class="ad__line ad__start">Starting the New Year</p>
    <p class="ad__line ad__red">IN THE RED</p>
    <p class="brand">Airwave<br>Harbor</p>
    <div class="help">
      <p class="help__title">Airwave Harbor <em>can help!</em></p>
      <ul class="help__list">
        <li class="help__item">Improve your NTR</li>
        <li class="help__item">Improve your cash flow</li>
        <li class="help__item">Improve your technology and operations</li>
      </ul>
    </div>
  </section>

</main>
</body>
</html>
```